Tallpine Facility Upkeep Systems

I need a full website built that must work on destkop and mobile. I have the logo's and will upload them however some stock industrial photos will be required. I will be hosting it on wix/godaddy for use with dynamics 365. Pretty simple requirements:

*Splash page
*What We Do
*How We do it
*Who Are We?
*Software
*Partnerships
*Contact: Includes twitter/insta and email/addy/phone

The site should be more scroll oriented with fewer tabs to allow for a improved mobile experience.
We're also looking for ways to improve our inbound marketing and would want to include various areas to get in touch /or collect their info. Look to www.kelnarova.com as an example of inbound marketing.
Images should be representative of the verticals we're focused on.

I have most of the content.

Target Market(s)

Asset intensive industries: Mining, Oil and Gas, Forest Products and Manufacturing.

Industry/Entity Type

Asset Management

Coding

Coded - Design and coding required

Number of Pages Required

5+ page

Font styles to use
Sans Serif

Requirements
Must have
• Must be easy to view and navigate on mobile and desktop.
Nice to have
• Employee/Customer portal.
Should not have
• Anything that will not display well in a mobile environment.

```html
<!DOCTYPE html>
<html lang="en">
<head>
<meta charset="utf-8">
<title>Tallpine FUS — Facility Upkeep Systems</title>
<link rel="stylesheet" href="https://fonts.googleapis.com/css2?family=Montserrat:wght@400;500;600&family=Open+Sans:wght@400;600&display=swap">
<style>
  :root {
    --olive: #8d9a5c;
    --olive-dark: #6f7c45;
    --navy: #1c3d5c;
    --band: #1f4a6d;
    --ink: #2b2b2b;
    --muted: #666a6e;
    --grey-bg: #efefef;
    --footer-bg: #f3f3f3;
    --line: #d9d9d9;
    --white: #ffffff;
  }
  * { box-sizing: border-box; margin: 0; padding: 0; }
  html, body { width: 1200px; height: 3750px; overflow: hidden; }
  body { font-family: "Open Sans", Arial, sans-serif; color: var(--ink); background: var(--white); position: relative; }
  h1, h2, h3, h4 { font-family: "Montserrat", Arial, sans-serif; font-weight: 500; }
  ul { list-style: none; }

  /* Hero */
  .hero { position: absolute; left: 0; top: 0; width: 1200px; height: 580px; }
  .hero-photo { position: absolute; inset: 0; background: radial-gradient(ellipse at 78% 35%, #7a7e82 0%, #3d4247 35%, #1f2326 70%, #15181a 100%); }
  .site-header { position: absolute; left: 100px; right: 100px; top: 40px; display: flex; justify-content: space-between; align-items: center; }
  .brand { display: flex; align-items: center; gap: 12px; color: var(--white); font-family: "Montserrat", Arial, sans-serif; font-size: 34px; font-weight: 400; letter-spacing: 1px; }
  .brand-mark { width: 16px; height: 16px; background: var(--white); }
  .main-nav { display: flex; gap: 30px; font-family: "Montserrat", Arial, sans-serif; font-size: 13.5px; font-weight: 500; color: var(--white); }
  .main-nav a { color: inherit; text-decoration: none; padding-bottom: 8px; }
  .main-nav a.active { color: #d6df9c; border-bottom: 2px solid var(--olive); }
  .hero-copy { position: absolute; left: 100px; top: 232px; color: var(--white); }
  .hero-copy h1 { font-size: 40px; line-height: 48px; font-weight: 500; letter-spacing: 1px; }
  .btn-olive { display: inline-block; margin-top: 20px; background: var(--olive); color: var(--white); font-family: "Montserrat", Arial, sans-serif; font-size: 15px; font-weight: 500; padding: 9px 22px; letter-spacing: .5px; }
  .slider-dots { display: flex; gap: 7px; margin-top: 38px; }
  .slider-dots span { width: 12px; height: 12px; border-radius: 50%; background: var(--white); }

  .section-title { text-align: center; font-size: 31px; letter-spacing: 1px; color: #222; }

  /* Employee drivers */
  .employee { position: absolute; left: 0; top: 580px; width: 1200px; height: 828px; }
  .employee .section-title { margin-top: 50px; }
  .driver-cols { display: flex; gap: 0; margin: 55px 0 0 100px; }
  .driver-col { width: 375px; }
  .driver-head { display: flex; align-items: center; gap: 14px; }
  .driver-head h3 { font-size: 15px; line-height: 20px; color: #444; text-transform: uppercase; }
  .badge { width: 66px; height: 66px; flex: none; }
  .dot-list { margin-top: 20px; font-size: 12px; color: var(--muted); line-height: 21px; }
  .dot-list li { position: relative; padding-left: 18px; }
  .dot-list li::before { content: ""; position: absolute; left: 0; top: 6px; width: 9px; height: 9px; border-radius: 50%; background: var(--olive); }
  .laptop { position: absolute; left: 300px; top: 420px; width: 594px; height: 350px; border-radius: 14px 14px 6px 6px; background: linear-gradient(180deg, #e9ece6 0%, #cdd5c2 55%, #9fb0a6 100%); }

  /* Project approach */
  .approach { position: absolute; left: 0; top: 1408px; width: 1200px; height: 427px; background: linear-gradient(180deg, #27577d 0%, var(--band) 100%); color: var(--white); }
  .approach .section-title { color: var(--white); margin-top: 80px; }
  .approach-cols { display: flex; margin: 60px 0 0 100px; }
  .approach-col { width: 375px; }
  .approach-col:nth-child(3) { margin-left: -30px; }
  .approach-head { display: flex; align-items: center; gap: 14px; }
  .approach-head h3 { font-size: 20px; }
  .approach .dot-list { color: #e8eef3; margin-top: 14px; }

  /* What is */
  .what { position: absolute; left: 0; top: 1835px; width: 1200px; height: 610px; }
  .what .section-title { margin-top: 80px; }
  .what p { width: 760px; margin: 22px auto 0; text-align: center; font-size: 12.5px; line-height: 21px; color: #444; }
  .browser { position: absolute; left: 260px; top: 235px; width: 680px; height: 375px; border: 1px solid var(--line); border-bottom: none; background: var(--white); box-shadow: 0 0 6px rgba(0,0,0,.12); }
  .browser-bar { height: 26px; background: #eceded; border-bottom: 1px solid var(--line); display: flex; align-items: center; gap: 5px; padding-left: 10px; }
  .browser-bar i { width: 8px; height: 8px; border-radius: 50%; display: block; }
  .browser-chart { position: absolute; left: 40px; top: 46px; width: 600px; height: 300px; background: linear-gradient(90deg, #3f7a34 0%, #6b9a3f 45%, #148a86 60%, #0f7d7c 100%); }

  /* Business drivers */
  .business { position: absolute; left: 0; top: 2445px; width: 1200px; height: 435px; background: var(--grey-bg); }
  .business-copy { position: absolute; left: 175px; top: 62px; width: 400px; }
  .business-copy h2 { font-size: 31px; letter-spacing: 1px; color: #222; }
  .business-copy p { margin-top: 14px; font-size: 12px; line-height: 18px; color: var(--muted); }
  .business-copy .dot-list { margin-top: 10px; }
  .business-art { position: absolute; left: 600px; top: 80px; width: 420px; height: 320px; background: linear-gradient(160deg, #d8dde2 0%, #9aa3ad 45%, #e8893a 100%); }

  /* Contact */
  .contact { position: absolute; left: 0; top: 2880px; width: 1200px; height: 510px; }
  .contact .section-title { margin-top: 90px; }
  .contact-form { position: absolute; left: 250px; top: 165px; width: 700px; }
  .form-row { display: flex; gap: 14px; margin-bottom: 12px; }
  .field { flex: 1; height: 40px; border: 1px solid #cfd3d6; font-size: 11.5px; color: #444; padding: 12px 14px; }
  .field.message { height: 112px; }
  .btn-navy { position: absolute; left: 293px; top: 233px; width: 114px; height: 38px; background: var(--navy); color: var(--white); font-family: "Montserrat", Arial, sans-serif; font-size: 15px; font-weight: 600; text-align: center; line-height: 38px; border-radius: 3px; }

  /* Footer */
  .site-footer { position: absolute; left: 0; top: 3390px; width: 1200px; height: 300px; background: var(--footer-bg); border-top: 1px solid #e2e2e2; }
  .footer-col { position: absolute; top: 70px; }
  .footer-col h4 { font-size: 17px; color: #333; letter-spacing: .5px; }
  .footer-brand { left: 100px; top: 80px; width: 260px; }
  .footer-brand .brand { color: var(--navy); font-size: 26px; }
  .footer-brand .brand-mark { width: 13px; height: 13px; background: var(--navy); }
  .footer-brand p { margin-top: 30px; font-size: 12px; line-height: 18px; color: var(--muted); }
  .socials { display: flex; gap: 6px; margin-top: 12px; }
  .socials span { width: 26px; height: 26px; border: 1px solid #777; border-radius: 50%; }
  .newsletter { left: 408px; width: 250px; }
  .newsletter p { margin-top: 10px; font-size: 11.5px; line-height: 18px; color: var(--muted); }
  .newsletter .field { display: block; margin-top: 12px; width: 243px; height: 40px; background: var(--white); }
  .btn-sub { display: inline-block; margin-top: 16px; background: var(--navy); color: var(--white); font-family: "Montserrat", Arial, sans-serif; font-size: 13px; font-weight: 600; padding: 8px 14px; }
  .contact-info { left: 720px; width: 240px; }
  .contact-info li { display: flex; gap: 14px; margin-top: 18px; font-size: 12px; line-height: 18px; color: var(--muted); }
  .contact-info svg { flex: none; margin-top: 2px; }
  .quick-links { left: 995px; }
  .quick-links ul { margin-top: 10px; font-size: 11.5px; line-height: 24px; color: var(--muted); }
  .copyright { position: absolute; left: 0; top: 3690px; width: 1200px; height: 60px; border-top: 1px solid #e2e2e2; background: var(--footer-bg); text-align: center; font-size: 11.5px; line-height: 60px; color: #555; }
</style>
</head>
<body>

<section class="hero">
  <div class="hero-photo" role="img" aria-label="Dark industrial photo of a hand touching glowing gear icons"></div>
  <header class="site-header">
    <div class="brand"><span class="brand-mark"></span>TALLPINE FUS</div>
    <nav class="main-nav">
      <a class="active">HOME</a><a>WHAT WE DO</a><a>HOW WE DO IT</a><a>WHO ARE WE?</a><a>SOFTWARE</a><a>PARTNERSHIPS</a><a>CONTACT</a>
    </nav>
  </header>
  <div class="hero-copy">
    <h1>TALLPINE FUS<br>ENTERPRISE</h1>
    <span class="btn-olive">READ MORE</span>
    <div class="slider-dots"><span></span><span></span><span></span></div>
  </div>
</section>

<section class="employee">
  <h2 class="section-title">WHY EMPLOYEE DRIVERS</h2>
  <div class="driver-cols">
    <div class="driver-col">
      <div class="driver-head">
        <svg class="badge" viewBox="0 0 66 66"><circle cx="33" cy="33" r="30" fill="none" stroke="#8d9a5c" stroke-width="6" stroke-dasharray="7 4"/><circle cx="33" cy="33" r="24" fill="#8d9a5c"/><rect x="21" y="27" width="24" height="16" rx="2" fill="#fff"/><rect x="28" y="23" width="10" height="5" fill="none" stroke="#fff" stroke-width="2"/></svg>
        <h3>Executive &amp; Operations<br>Managers</h3>
      </div>
      <ul class="dot-list">
        <li>More reliable operations.</li>
        <li>Increased efficiency and profitability.</li>
        <li>Reduced and reliable maintenance costs.</li>
        <li>Reduced liability/risk.</li>
        <li>Manage by knowledge (reduce surprises).</li>
        <li>Better Budgeting.</li>
      </ul>
    </div>
    <div class="driver-col">
      <div class="driver-head">
        <svg class="badge" viewBox="0 0 66 66"><circle cx="33" cy="33" r="30" fill="none" stroke="#8d9a5c" stroke-width="6" stroke-dasharray="7 4"/><circle cx="33" cy="33" r="24" fill="#8d9a5c"/><path d="M23 43 L37 29" stroke="#fff" stroke-width="5" stroke-linecap="round"/><circle cx="39" cy="27" r="7" fill="none" stroke="#fff" stroke-width="3"/></svg>
        <h3>Maintenance<br>Managers</h3>
      </div>
      <ul class="dot-list">
        <li>Better information.</li>
        <li>Better organization, decisions and justifications.</li>
        <li>Identify where to spend money most effectively.</li>
      </ul>
    </div>
    <div class="driver-col">
      <div class="driver-head">
        <svg class="badge" viewBox="0 0 66 66"><circle cx="33" cy="33" r="30" fill="none" stroke="#8d9a5c" stroke-width="6" stroke-dasharray="7 4"/><circle cx="33" cy="33" r="24" fill="#8d9a5c"/><circle cx="33" cy="27" r="6" fill="#fff"/><path d="M21 45 Q33 30 45 45 Z" fill="#fff"/></svg>
        <h3>Maintenance<br>Workers</h3>
      </div>
      <ul class="dot-list">
        <li>Easier to prevent messes before they happen.</li>
        <li>Get information, not the runaround.</li>
        <li>Spend time working on the right things.</li>
      </ul>
    </div>
  </div>
  <div class="laptop" role="img" aria-label="Laptop showing a capabilities and value proposition chart"></div>
</section>

<section class="approach">
  <h2 class="section-title">HOW PROJECT APPROACH</h2>
  <div class="approach-cols">
    <div class="approach-col">
      <div class="approach-head">
        <svg class="badge" viewBox="0 0 66 66"><circle cx="33" cy="33" r="30" fill="none" stroke="#fff" stroke-width="6" stroke-dasharray="7 4"/><circle cx="33" cy="33" r="24" fill="#fff"/><path d="M20 28 L33 20 L46 28 Z M22 30h22v2H22z M24 33h3v9h-3z M31.5 33h3v9h-3z M39 33h3v9h-3z M21 43h24v3H21z" fill="#1f4a6d"/></svg>
        <h3>THREE PILLARS</h3>
      </div>
      <ul class="dot-list">
        <li>Maintenance &amp; Reliability</li>
        <li>Inventory &amp; Stores</li>
        <li>Procurement &amp; Payables(Three Pillars</li>
      </ul>
    </div>
    <div class="approach-col">
      <div class="approach-head">
        <svg class="badge" viewBox="0 0 66 66"><circle cx="33" cy="33" r="30" fill="none" stroke="#fff" stroke-width="6" stroke-dasharray="7 4"/><circle cx="33" cy="33" r="24" fill="#fff"/><rect x="22" y="22" width="10" height="10" fill="#1f4a6d"/><rect x="34" y="22" width="10" height="10" fill="#1f4a6d"/><rect x="22" y="34" width="10" height="10" fill="#1f4a6d"/></svg>
        <h3>THREE PHASES</h3>
      </div>
      <ul class="dot-list">
        <li>Pre-Feasibility</li>
        <li>Feasibility</li>
        <li>Execution</li>
      </ul>
    </div>
    <div class="approach-col">
      <div class="approach-head">
        <svg class="badge" viewBox="0 0 66 66"><circle cx="33" cy="33" r="30" fill="none" stroke="#fff" stroke-width="6" stroke-dasharray="7 4"/><circle cx="33" cy="33" r="24" fill="#fff"/><circle cx="33" cy="26" r="6" fill="none" stroke="#1f4a6d" stroke-width="3"/><circle cx="26" cy="38" r="6" fill="none" stroke="#1f4a6d" stroke-width="3"/><circle cx="40" cy="38" r="6" fill="none" stroke="#1f4a6d" stroke-width="3"/></svg>
        <h3>THREE DIMENSIONS</h3>
      </div>
      <ul class="dot-list">
        <li>People &amp; Process</li>
        <li>Physical</li>
        <li>Technical</li>
      </ul>
    </div>
  </div>
</section>

<section class="what">
  <h2 class="section-title">WHAT IS TALLPINE FUS</h2>
  <p>Tallpine Facility Upkeep Systems is a boutique firm specializing in maintenance and reliability, supply chain, business intelligence and program management for asset intensive industries. We represent the finest people, process and technology tools to achieve greater results.</p>
  <div class="browser">
    <div class="browser-bar"><i style="background:#e0605a"></i><i style="background:#e8b94a"></i><i style="background:#67c04d"></i></div>
    <div class="browser-chart" role="img" aria-label="Chart of inventory capabilities, value proposition and role of inventory management"></div>
  </div>
</section>

<section class="business">
  <div class="business-copy">
    <h2>WHY BUSINESS DRIVERS</h2>
    <p>Sed ut perspiciatis unde omnis iste natus error sit voluptatem accusantium doloremque laudantium, totam rem aperiam, eaque ipsa</p>
    <ul class="dot-list">
      <li>Improved planned &amp; scheduled maintenance</li>
      <li>Uptime improvements</li>
      <li>Longevity and safety of equipment</li>
      <li>Optimized asset performance</li>
      <li>Administrative savings</li>
      <li>Improved inventory levels</li>
      <li>Skills portability, increased employee morale</li>
    </ul>
  </div>
  <div class="business-art" role="img" aria-label="Flat illustration of hands typing on a keyboard beside a monitor and a coffee cup"></div>
</section>

<section class="contact">
  <h2 class="section-title">CONTACT US</h2>
  <form class="contact-form">
    <div class="form-row"><div class="field">Name :</div><div class="field">Phone :</div></div>
    <div class="form-row"><div class="field">Email :</div><div class="field">Subject :</div></div>
    <div class="form-row"><div class="field message">Message :</div></div>
    <div class="btn-navy">SUBMIT</div>
  </form>
</section>

<footer class="site-footer">
  <div class="footer-col footer-brand">
    <div class="brand"><span class="brand-mark"></span>TALLPINE FUS</div>
    <p>Sed ut perspiciatis unde omnis iste natus error sit voluptatem accusantium doloremque laudantium, totam rem aperiam.</p>
    <div class="socials"><span></span><span></span><span></span><span></span></div>
  </div>
  <div class="footer-col newsletter">
    <h4>SIGN UP FOR NEWSLETTER</h4>
    <p>Excepteur sint occaecat cupidatat non proident, sunt in culpa qui officia deserunt</p>
    <div class="field">Enter email</div>
    <span class="btn-sub">SUBSCRIPTION</span>
  </div>
  <div class="footer-col contact-info">
    <h4>CONTACT US</h4>
    <ul>
      <li><svg width="14" height="18" viewBox="0 0 14 18"><path d="M7 0a7 7 0 0 0-7 7c0 5 7 11 7 11s7-6 7-11a7 7 0 0 0-7-7z" fill="#666"/><circle cx="7" cy="7" r="2.5" fill="#fff"/></svg><span>Tallpine FUS<br>418 Ridgeline Way, Corvale, NC,<br>27390</span></li>
      <li><svg width="14" height="16" viewBox="0 0 14 16"><path d="M3 0 L6 4 L4 6 Q6 10 9 12 L11 10 L14 13 L12 16 Q3 14 0 3 Z" fill="#666"/></svg><span>Phone: 555.010.0199</span></li>
      <li><svg width="14" height="12" viewBox="0 0 14 12"><rect width="14" height="12" fill="#666"/><path d="M0 0 L7 6 L14 0" fill="none" stroke="#fff" stroke-width="1.5"/></svg><span>Email: info@tallpineupkeep.com</span></li>
    </ul>
  </div>
  <div class="footer-col quick-links">
    <h4>QUICK LINKS</h4>
    <ul><li>Home</li><li>What we do</li><li>How We do it</li><li>Who are we?</li><li>Software</li><li>Partnerships</li><li>Contact</li></ul>
  </div>
</footer>
<div class="copyright">©2015 - 2016 Tallpine FUS. All Rights Reserved.</div>

</body>
</html>
```